Tallmark Benefit Advisors Business Card Design

I already placed order for cards through press grove.

Double sided- back Navy with White logo and raised silver "swoosh"

```html
<!DOCTYPE html>
<html lang="en">
<head>
<meta charset="utf-8">
<title>Tallmark Benefit Advisors – Business Card</title>
<link href="https://fonts.googleapis.com/css2?family=Montserrat:wght@400;500;700&display=swap" rel="stylesheet">
<style>
  :root {
    --navy: #0f2249;
    --white: #ffffff;
    --ink: #2b2b2b;
    --backdrop: #3a3a3a;
    --silver-dark: #6d6d6d;
    --silver-light: #e2e2e2;
  }
  * { margin: 0; padding: 0; box-sizing: border-box; }
  html, body {
    width: 1200px; height: 1059px; overflow: hidden;
    background: var(--backdrop);
    font-family: "Montserrat", sans-serif;
  }
  .card {
    position: absolute;
    width: 690px; height: 394px;
    border-radius: 22px;
    overflow: hidden;
  }
  .card--front { left: 256px; top: 100px; background: var(--white); }
  .card--back { left: 254px; top: 536px; background: var(--navy); }

  .accent-bar {
    position: absolute; top: 92px; height: 212px;
  }
  .accent-bar--navy { left: 0; width: 27px; background: var(--navy); }
  .accent-bar--silver {
    right: 0; width: 24px;
    background: linear-gradient(180deg, var(--silver-dark) 0%, var(--silver-light) 45%, var(--silver-dark) 100%);
  }

  .brand {
    position: absolute;
    text-align: center;
    color: var(--navy);
    font-weight: 500;
  }
  .brand span { display: block; }
  .brand--front { left: 50px; width: 290px; top: 166px; }
  .brand--front .brand__name { font-size: 30px; letter-spacing: 2px; line-height: 1; }
  .brand--front .brand__sub { font-size: 9px; letter-spacing: 5px; margin-top: 6px; }

  .divider { position: absolute; width: 2px; }
  .divider--front { left: 354px; top: 92px; height: 212px; background: var(--navy); }

  .contact { position: absolute; left: 378px; top: 86px; color: var(--ink); }
  .contact__name { font-size: 33px; font-weight: 700; color: var(--navy); letter-spacing: 0.3px; line-height: 1.1; }
  .contact__title { font-size: 18px; margin-top: 2px; }
  .contact__address { font-size: 18px; line-height: 28px; margin-top: 10px; }
  .contact__list { list-style: none; margin-top: 10px; }
  .contact__list li { font-size: 18px; line-height: 27.5px; display: flex; align-items: center; gap: 8px; }
  .contact__list svg { width: 15px; height: 15px; fill: var(--navy); flex: none; }

  .brand--back { left: 0; width: 690px; top: 150px; color: var(--white); }
  .brand--back .brand__name { font-size: 64px; letter-spacing: 4px; line-height: 1; }
  .brand--back .brand__sub { font-size: 15px; letter-spacing: 11px; margin-top: 12px; }
</style>
</head>
<body>
  <section class="card card--front">
    <div class="accent-bar accent-bar--navy"></div>
    <div class="brand brand--front">
      <span class="brand__name">TALLMARK</span>
      <span class="brand__sub">BENEFIT ADVISORS</span>
    </div>
    <div class="divider divider--front"></div>
    <div class="contact">
      <h1 class="contact__name">DANIEL HART</h1>
      <p class="contact__title">Managing Director</p>
      <p class="contact__address">Your address, City<br>State, Zip 1234</p>
      <ul class="contact__list">
        <li><svg viewBox="0 0 16 16"><path d="M2 6c0-2 3-3 6-3s6 1 6 3v1h-3V6H5v1H2z M4 8h8l2 5H2z"/></svg>123 456 789</li>
        <li><svg viewBox="0 0 16 16"><path d="M1 3h14v2L8 9 1 5z M1 7l7 4 7-4v6H1z"/></svg>info@youremail.com</li>
        <li><svg viewBox="0 0 16 16"><circle cx="8" cy="8" r="7"/></svg>www.yourwebsite.com</li>
      </ul>
    </div>
    <div class="accent-bar accent-bar--silver"></div>
  </section>

  <section class="card card--back">
    <div class="brand brand--back">
      <span class="brand__name">TALLMARK</span>
      <span class="brand__sub">BENEFIT ADVISORS</span>
    </div>
  </section>
</body>
</html>
```